Paper Lantern Theory - Podcast Cover

Paper Lantern Theory is a weekly podcast that dispels some of the myths about conventional economic thinking and provides a new way of thinking about issues that are faced by the global economy. It's insightful, thought-provoking and, most importantly, fun. We are refreshing the look and sound of the podcast. I have attached a copy of the old amateur design (which I did!)

Target Market(s)

Male oriented, smart folk with an interest in politics and economics

Font styles to use
Sans Serif

Requirements
Must have
• Clearly visible title, even when reduced in size. Must be 3000 pixels by 3000 pixels.
Nice to have
• This podcast challenges the status quo. It should reflect that. Photos and names of the hosts. Actually, because th ephotos are so different, we'd be open to the idea of a caricature if you can do that within the price.

```html
<!DOCTYPE html>
<html lang="en">
<head>
<meta charset="utf-8">
<title>Paper Lantern Theory – Podcast Cover</title>
<link rel="stylesheet" href="https://fonts.googleapis.com/css2?family=Anton&family=Poppins:wght@500;600&display=swap">
<style>
  :root {
    --page: #d9d9d9;
    --cream: #fefdc8;
    --navy: #252a44;
    --slate: #2e4a5a;
    --cyan: #00a9d0;
    --amber: #f5a81c;
    --scene: #e6dfa6;
  }
  * { margin: 0; padding: 0; box-sizing: border-box; }
  html, body { width: 1200px; height: 1105px; overflow: hidden; }
  body { background: var(--page); position: relative; font-family: "Poppins", sans-serif; }

  .cover {
    position: absolute; left: 180px; top: 132px;
    width: 840px; height: 840px;
    background: var(--cream); overflow: hidden;
  }
  .cover-layer { position: absolute; inset: 0; }

  .meeting-scene {
    position: absolute; left: 78px; top: 361px; width: 693px; height: 242px;
    background: radial-gradient(ellipse at 50% 55%, var(--scene) 0%, rgba(230,223,166,0.5) 55%, rgba(254,253,200,0) 80%);
  }

  .role-label {
    position: absolute; top: 480px; width: 184px; height: 33px;
    border-top: 2px solid var(--amber); border-bottom: 2px solid var(--amber);
    display: flex; align-items: center; justify-content: center;
    font-weight: 500; font-size: 19px; letter-spacing: 2px; color: var(--navy);
  }
  .role-label--left { left: 103px; }
  .role-label--right { left: 554px; }

  .host-name {
    position: absolute; top: 639px; font-weight: 600; font-size: 19px;
    white-space: nowrap; color: var(--navy); line-height: 1;
  }
  .host-name .surname { color: var(--cyan); }
  .host-name--left { left: 264px; }
  .host-name--right { left: 441px; }
</style>
</head>
<body>
  <main class="cover">
    <svg class="cover-layer" width="840" height="840" viewBox="0 0 840 840">
      <path class="corner-band" d="M0 0 H840 V190 C810 90 740 30 640 23 H0 Z" fill="var(--slate)"/>
      <path class="corner-edge" d="M0 23 H640 C740 30 810 90 840 190" fill="none" stroke="var(--navy)" stroke-width="2"/>
      <text class="title-top" x="125" y="213" textLength="590" lengthAdjust="spacingAndGlyphs"
            font-family="Anton, sans-serif" font-size="134" fill="var(--cyan)">PAPER LANTERN</text>
      <text class="title-bottom" x="125" y="331" textLength="590" lengthAdjust="spacingAndGlyphs"
            font-family="Anton, sans-serif" font-size="134" fill="var(--navy)">THEORY</text>
    </svg>

    <div class="meeting-scene" role="img" aria-label="Faint silhouettes of people in a meeting around a table"></div>

    <div class="role-label role-label--left">PROFESSOR</div>
    <div class="role-label role-label--right">PODCAST HOST</div>

    <svg class="cover-layer" width="840" height="840" viewBox="0 0 840 840">
      <defs>
        <linearGradient id="tone-professor" x1="0" y1="0" x2="0" y2="1">
          <stop offset="0" stop-color="#b9b2a6"/>
          <stop offset="0.45" stop-color="#e9e6de"/>
          <stop offset="1" stop-color="#d8d5cf"/>
        </linearGradient>
        <linearGradient id="tone-host" x1="0" y1="0" x2="0" y2="1">
          <stop offset="0" stop-color="#e0b39e"/>
          <stop offset="0.45" stop-color="#4fa3b3"/>
          <stop offset="1" stop-color="#3a8ea0"/>
        </linearGradient>
      </defs>
      <path class="host-photo host-photo--left" role="img" aria-label="Photo of Martin Hale, the professor, in a white t-shirt"
            fill="url(#tone-professor)"
            d="M131 590 C131 555 160 537 190 537 C225 537 247 560 247 600 L243 680 C280 700 305 720 312 760 L317 840 L36 840 L48 760 C60 720 100 700 140 690 Z"/>
      <path class="host-photo host-photo--right" role="img" aria-label="Photo of Nigel Ford, the podcast host, in a teal polo shirt"
            fill="url(#tone-host)"
            d="M588 600 C588 560 610 531 646 531 C684 531 706 560 706 600 L704 650 C740 670 790 690 800 730 L811 840 L471 840 L476 760 C490 700 560 680 594 660 Z"/>

      <g class="name-bracket" fill="none" stroke="var(--navy)" stroke-width="1.6">
        <path d="M299 625 H393 V664 H352"/>
        <path d="M535 625 H431 V665 H476"/>
      </g>
      <g class="name-dots" fill="var(--navy)">
        <circle cx="299" cy="625" r="3.5"/>
        <circle cx="535" cy="625" r="3.5"/>
        <circle cx="333" cy="665" r="2"/><circle cx="340" cy="665" r="2"/><circle cx="347" cy="665" r="2"/>
        <circle cx="481" cy="666" r="2"/><circle cx="488" cy="666" r="2"/><circle cx="495" cy="666" r="2"/>
      </g>
    </svg>

    <p class="host-name host-name--left">MARTIN <span class="surname">HALE</span></p>
    <p class="host-name host-name--right">NIGEL <span class="surname">FORD</span></p>
  </main>
</body>
</html>
```